Fahrzeugbeschriftung für zertifizierten metall- und kunststoffverarbeitenden Betrieb
Zielgruppe
Haldrek Feinmechanik GmbH | CAD CAM | CNC Drehteile | CNC Frästeile | Lohnfertigung | Konstruktion
Aufgabenstellung
Fahrzeugwerbung auf Varenz Kastor

```html
<!DOCTYPE html>
<html lang="de">
<head>
<meta charset="utf-8">
<title>Haldrek Feinmechanik – Fahrzeugbeschriftung</title>
<link rel="stylesheet" href="https://fonts.googleapis.com/css2?family=Poppins:wght@300;400;500;600&display=swap">
<style>
  :root {
    --stage: #f1f0ee;
    --wrap-dark: #2c2e30;
    --wrap-light: #ececec;
    --brand-navy: #1f3a55;
    --brand-red: #e2312f;
    --text-light: #f2f2f2;
    --text-silver: #d9d9d9;
  }
  * { margin: 0; padding: 0; box-sizing: border-box; }
  html, body {
    width: 1200px; height: 675px; overflow: hidden;
    background: var(--stage);
    font-family: "Poppins", sans-serif;
  }
  .vehicle-side {
    position: absolute; left: 40px; top: 200px;
    width: 1110px; height: 385px;
    background: var(--wrap-dark);
    border-radius: 120px 28px 18px 40px;
    overflow: hidden;
  }
  .brand-band {
    position: absolute; left: 402px; top: 0;
    width: 322px; height: 100%;
    background: var(--wrap-light);
    display: flex; align-items: center; justify-content: center;
  }
  .brand-band__name {
    font-weight: 600; font-size: 56px; letter-spacing: -1px; line-height: 1;
    color: var(--brand-navy);
  }
  .phone {
    position: absolute; left: 188px; top: 222px;
    display: flex; align-items: center; gap: 8px;
    color: var(--text-light); font-size: 15px; font-weight: 400; letter-spacing: 0.3px;
  }
  .phone svg { width: 20px; height: 20px; }
  .company {
    position: absolute; left: 733px; top: 0;
    width: 280px; height: 190px; text-align: right;
  }
  .company > * { position: absolute; right: 0; white-space: nowrap; }
  .company__name {
    top: 4px;
    font-weight: 600; font-size: 70px; line-height: 1; letter-spacing: -2px;
    color: var(--text-silver);
  }
  .company__legal {
    top: 84px;
    font-weight: 300; font-size: 25px; line-height: 1;
    color: var(--text-silver);
  }
  .company__services {
    top: 118px; line-height: 20px;
    font-weight: 500; font-size: 16px; color: var(--brand-red);
  }
  .company__fields {
    top: 143px; line-height: 16px;
    font-weight: 500; font-size: 12.5px; letter-spacing: 0.3px;
    color: var(--text-light);
  }
  .web-band {
    position: absolute; left: 733px; top: 194px;
    width: 377px; height: 38px;
    background: var(--brand-red);
    color: #fff; font-weight: 500; font-size: 16.5px; letter-spacing: 0.2px;
    display: flex; align-items: center; padding-left: 18px;
  }
</style>
</head>
<body>
  <main class="vehicle-side">
    <div class="phone">
      <svg viewBox="0 0 20 20" aria-hidden="true">
        <circle cx="10" cy="10" r="9" fill="none" stroke="currentColor" stroke-width="1.4"/>
        <path d="M7 5.5c.6-.4 1.2-.2 1.5.4l.7 1.4c.2.5 0 1-.4 1.3l-.5.3c.4 1.1 1.2 2 2.2 2.6l.4-.4c.4-.4.9-.5 1.3-.2l1.3.8c.5.3.6 1 .2 1.5-.7.9-1.8 1.1-2.8.6-2.300-1.1-3.9-3-4.6-5.3-.3-1.1 0-2.3.7-3z" fill="currentColor"/>
      </svg>
      <span>07431 558260</span>
    </div>

    <section class="brand-band">
      <span class="brand-band__name">haldrek.</span>
    </section>

    <section class="company">
      <h1 class="company__name">haldrek.</h1>
      <p class="company__legal">feinmechanik gmbh</p>
      <p class="company__services">CAD CAM | CNC Drehteile | CNC</p>
      <p class="company__fields">KONSTRUKTION | ENTWICKLUNG | DESIGN</p>
    </section>

    <div class="web-band">HALDREK-FEINMECHANIK.DE</div>
  </main>
</body>
</html>
```